Lunaform website scandinavian interior design

Existing website: http://lunaform-example.no/

Webdesign for interior designer Ragna Tveitmo. The company name is Lunaform. Scandinavian interiør is known to be simple and elegant. The website will be in Norwegian, we are working on the text. The website needs to have a few more pages than just the front page. Here are the different titles of the pages:

1. Hjem
2. Om Lunaform
3. Tjenester og priser
4.. Kontakt oss

There should be Chatterloop and Pixelane icons somewhere at the bottom of the website.

The logo we want to use is attached (pink with black print, see attachment )

We have attached images for inspiration. We want to use some of these colors. The color in the logo, The style should be elegant, modern and delicate.

It is imprtant that the website is user friendly.

Target Market(s)

People who want to decorate their home
Companies and public sector who need to redecorate

Industry/Entity Type

Interior Designer

Coding

Coded - Design and coding required

Number of Pages Required

5+ page

Font styles to use
Other font styles liked:
• see example in the logo breakdown

Requirements
Must have
• Elegant, modern and delicate design
Images of design, see examples attached
Colors similar to the pictures
Should not have
• Too bright colors
Pictures of people

```html
<!DOCTYPE html>
<html lang="en">
<head>
<meta charset="utf-8">
<title>Lunaform – Farge &amp; Interiørdesign</title>
<link href="https://fonts.googleapis.com/css2?family=Cormorant+Garamond:wght@500;600&family=Lato:ital,wght@0,400;1,400&display=swap" rel="stylesheet">
<style>
:root{
  --page:#fbf8f5;
  --ink:#2a1512;
  --text:#3b2e2a;
  --blush:#ecd3c8;
  --blush-line:#cfa79a;
  --field:#ffffff;
  --field-line:#ddd3cf;
  --white:#ffffff;
}
*{box-sizing:border-box;margin:0;padding:0}
html,body{width:1200px;height:3183px;overflow:hidden}
body{background:var(--page);color:var(--text);font-family:'Lato',sans-serif;position:relative}
.serif{font-family:'Cormorant Garamond',serif}
.abs{position:absolute}

/* header */
.site-header{position:absolute;left:0;top:0;width:1200px;height:105px}
.phone{left:40px;top:44px;display:flex;align-items:center;gap:10px;font-family:'Cormorant Garamond',serif;font-size:14px;font-weight:600;color:var(--ink)}
.nav-link{top:45px;font-family:'Cormorant Garamond',serif;font-weight:600;font-size:14.5px;letter-spacing:.3px;color:var(--ink);text-decoration:none}
.brand{left:520px;top:34px;width:150px;text-align:center;font-family:'Cormorant Garamond',serif;font-weight:600;font-size:30px;color:var(--ink);letter-spacing:1px}
.lang{left:1124px;top:40px;width:37px;height:24px;border:1px solid var(--ink);font-family:'Cormorant Garamond',serif;font-weight:600;font-size:13px;color:var(--ink);display:flex;align-items:center;justify-content:center;gap:2px}

/* hero */
.hero{left:37px;top:105px;width:1125px;height:620px;background:linear-gradient(100deg,#d9b78e 0%,#c9a57b 22%,#dedbd4 45%,#e9e7e3 60%,#b5b59c 78%,#6f7b52 100%)}
.hero-shade{position:absolute;inset:0;background:linear-gradient(180deg,rgba(0,0,0,.05),rgba(0,0,0,.12))}
.hero-kicker{left:0;width:1125px;top:240px;text-align:center;color:var(--white);font-family:'Cormorant Garamond',serif;font-weight:500;font-size:28px;letter-spacing:1.5px}
.hero-rule{left:266px;top:279px;width:585px;height:1px;background:var(--white)}
.hero-title{left:0;width:1125px;top:278px;text-align:center;color:var(--white);font-family:'Cormorant Garamond',serif;font-weight:600;font-size:72px;letter-spacing:2px}
.btn{display:flex;align-items:center;justify-content:center;font-family:'Cormorant Garamond',serif;font-weight:600;font-size:14.5px;letter-spacing:.5px;text-transform:uppercase}
.btn-dark{background:var(--ink);color:var(--white)}
.btn-blush{background:var(--blush);color:var(--ink)}
.dots{left:496px;top:581px;display:flex;gap:18px}
.dots span{width:20px;height:4px;background:var(--white)}
.dots span:first-child{opacity:.6}

/* about */
.about-photo{left:109px;top:818px;width:445px;height:451px;background:linear-gradient(180deg,#ececec 0%,#e2e2e2 65%,#cfc8c2 100%)}
.about-kicker{left:612px;top:848px;font-family:'Cormorant Garamond',serif;font-weight:500;font-size:38px;color:var(--ink);letter-spacing:1px}
.about-title{left:612px;top:900px;font-family:'Cormorant Garamond',serif;font-weight:600;font-size:62px;color:var(--ink);letter-spacing:1px}
.about-copy{left:615px;top:1014px;width:485px;font-size:13.5px;line-height:22.5px}
.about-copy p+p{margin-top:22px}

/* services */
.section-title{left:0;width:1200px;text-align:center;font-family:'Cormorant Garamond',serif;font-weight:500;font-size:40px;color:var(--ink);letter-spacing:1px}
.service{top:1443px;width:260px;text-align:center}
.service-ring{width:196px;height:196px;border:1px solid var(--ink);border-radius:50%;margin:0 auto;display:flex;align-items:center;justify-content:center}
.service-icon{width:78px;height:78px;border-radius:50%;background:#f1e1da}
.service h3{margin-top:30px;font-family:'Cormorant Garamond',serif;font-weight:600;font-size:19px;letter-spacing:1.2px;color:var(--ink)}
.service p{margin-top:10px;font-size:12px;line-height:18px;padding:0 22px}

/* cta band */
.cta{left:36px;top:1843px;width:1128px;height:482px;background:linear-gradient(90deg,#e6e4e3 0%,#e3e2e1 50%,#d4d3d2 75%,#c9c8c7 100%)}
.cta-floor{position:absolute;left:0;right:0;bottom:0;height:110px;background:linear-gradient(180deg,#e8e8e8,#f1f1f1)}
.cta-title{left:60px;top:118px;font-family:'Cormorant Garamond',serif;font-weight:600;font-size:40px;line-height:45px;letter-spacing:1.3px;color:var(--ink)}
.cta-copy{left:67px;top:232px;width:490px;font-size:13.5px;line-height:22.5px}

/* contact */
.field{background:var(--field);border:1px solid var(--field-line);font-style:italic;font-size:12.5px;color:#b6aca8;padding:12px 15px}

/* footer */
.site-footer{left:36px;top:2760px;width:1128px;height:387px;background:var(--blush)}
.footer-brand{left:60px;top:100px;width:272px;text-align:center;font-family:'Cormorant Garamond',serif;font-weight:600;font-size:54px;color:var(--ink);letter-spacing:1px}
.footer-head{top:70px;font-family:'Cormorant Garamond',serif;font-weight:600;font-size:18px;letter-spacing:1px;color:var(--ink)}
.footer-list{font-size:12.5px;line-height:22.5px;color:var(--ink);list-style:none}
.footer-row{display:flex;gap:10px;align-items:flex-start}
.social{list-style:none;display:flex;flex-direction:column;gap:9px}
.social li{display:flex;align-items:center;gap:8px;font-size:12.5px;color:var(--ink)}
.social i{width:22px;height:22px;border-radius:50%;background:var(--ink);display:block}
.footer-rule{left:60px;top:308px;width:1008px;height:1px;background:var(--ink)}
.copyright{left:0;width:1128px;top:342px;text-align:center;font-size:11.5px;color:var(--ink)}
</style>
</head>
<body>

<header class="site-header">
  <div class="abs phone">
    <svg width="18" height="18" viewBox="0 0 24 24" fill="none" stroke="#2a1512" stroke-width="1.4"><path d="M5 3h4l2 5-2.5 1.5a11 11 0 0 0 6 6L16 13l5 2v4a2 2 0 0 1-2 2A17 17 0 0 1 3 5a2 2 0 0 1 2-2z"/></svg>
    +4740012345
  </div>
  <a class="abs nav-link" style="left:284px">HOME</a>
  <a class="abs nav-link" style="left:351px">ABOUT LUNAFORM</a>
  <div class="abs brand">Lunaform</div>
  <a class="abs nav-link" style="left:711px">SERVICES AND PRICES</a>
  <a class="abs nav-link" style="left:879px">CONTACT US</a>
  <div class="abs lang">EN<svg width="7" height="5" viewBox="0 0 7 5"><path d="M.5.5 3.5 4 6.5.5" fill="none" stroke="#2a1512"/></svg></div>
</header>

<section class="abs hero" role="img" aria-label="Sunlit Scandinavian bedroom with a wooden platform bed, wood-panelled wall and garden view">
  <div class="hero-shade"></div>
  <div class="abs hero-kicker">IT`S AN AMAZING SERVICES</div>
  <div class="abs hero-rule"></div>
  <h1 class="abs hero-title">INTERIOR DESIGN</h1>
  <a class="abs btn btn-blush" style="left:425px;top:372px;width:131px;height:42px">Read more</a>
  <a class="abs btn btn-dark" style="left:567px;top:372px;width:133px;height:42px">Contact us</a>
  <div class="abs dots"><span></span><span></span><span></span><span></span></div>
</section>

<section class="about">
  <div class="abs about-photo" role="img" aria-label="Light living room with a tan leather sofa, empty picture frame and floor lamp"></div>
  <div class="abs about-kicker">ABOUT</div>
  <h2 class="abs about-title">LUNAFORM</h2>
  <div class="abs about-copy">
    <p>Lorem Ipsum is simply dummy text of the printing and typesetting industry. Lorem Ipsum has been the industry's standard dummy text ever since the 1500s, when an unknown printer took a galley of type and scrambled it to make a type specimen book.</p>
    <p>It has survived not only five centuries, but also the leap into electronic typesetting, remaining essentially unchanged.</p>
  </div>
  <a class="abs btn btn-dark" style="left:615px;top:1201px;width:131px;height:41px">Read more</a>
</section>

<section class="services">
  <h2 class="abs section-title" style="top:1348px">OUR SERVICES</h2>
  <div class="abs service" style="left:76px">
    <div class="service-ring"><div class="service-icon" role="img" aria-label="Chair icon"></div></div>
    <h3>INTERIOR DESIGN</h3>
    <p>Lorem Ipsum is simply dummy text of the printing and typesetting industry.</p>
  </div>
  <div class="abs service" style="left:338px">
    <div class="service-ring"><div class="service-icon" role="img" aria-label="Potted plant icon"></div></div>
    <h3>DECORATIVE SERVICE</h3>
    <p>Lorem Ipsum is simply dummy text of the printing and typesetting industry.</p>
  </div>
  <div class="abs service" style="left:603px">
    <div class="service-ring"><div class="service-icon" role="img" aria-label="Floor plan icon"></div></div>
    <h3>SPACE PLANNING</h3>
    <p>Lorem Ipsum is simply dummy text of the printing and typesetting industry.</p>
  </div>
  <div class="abs service" style="left:861px">
    <div class="service-ring"><div class="service-icon" role="img" aria-label="Gear and light bulb icon"></div></div>
    <h3>PROJECT MANAGEMENT</h3>
    <p>Lorem Ipsum is simply dummy text of the printing and typesetting industry.</p>
  </div>
</section>

<section class="abs cta" role="img" aria-label="Bright room with a grey sofa, cushions and a small potted plant on a white wooden floor">
  <div class="cta-floor"></div>
  <h2 class="abs cta-title">WANT YOU DECORATE<br>YOUR INTERIOR?</h2>
  <p class="abs cta-copy">Lorem Ipsum is simply dummy text of the printing and typesetting industry. Lorem Ipsum has been the industry's standard dummy text ever since the 1500s.</p>
  <a class="abs btn btn-dark" style="left:67px;top:311px;width:132px;height:41px">Contact us</a>
</section>

<section class="contact">
  <h2 class="abs section-title" style="top:2378px">CONTACT US</h2>
  <div class="abs field" style="left:329px;top:2461px;width:233px;height:42px">Full Name*</div>
  <div class="abs field" style="left:329px;top:2513px;width:233px;height:42px">Email*</div>
  <div class="abs field" style="left:329px;top:2567px;width:233px;height:41px">Phone*</div>
  <div class="abs field" style="left:575px;top:2461px;width:293px;height:147px">Message*</div>
  <a class="abs btn btn-dark" style="left:534px;top:2652px;width:132px;height:41px">Send now</a>
</section>

<footer class="abs site-footer">
  <div class="abs footer-brand">Lunaform</div>

  <h4 class="abs footer-head" style="left:409px">QUICK LINKS</h4>
  <ul class="abs footer-list" style="left:411px;top:130px">
    <li>Home</li><li>About Lunaform</li><li>Services and prices</li><li>Contact us</li>
  </ul>

  <h4 class="abs footer-head" style="left:643px">CONTACT US</h4>
  <div class="abs footer-list" style="left:645px;top:130px">
    <div class="footer-row">
      <svg width="12" height="14" viewBox="0 0 12 14" style="margin-top:5px" fill="none" stroke="#2a1512"><path d="M6 13S1.5 8.5 1.5 5.5a4.5 4.5 0 0 1 9 0C10.5 8.5 6 13 6 13z"/><circle cx="6" cy="5.5" r="1.6"/></svg>
      <div>Lunaform As v / Ragna Tveitmo<br>Lyngveien 14<br>3400 Eikstrand</div>
    </div>
    <div class="footer-row" style="margin-top:22px">
      <svg width="12" height="12" viewBox="0 0 24 24" style="margin-top:5px" fill="none" stroke="#2a1512" stroke-width="1.8"><path d="M5 3h4l2 5-2.5 1.5a11 11 0 0 0 6 6L16 13l5 2v4a2 2 0 0 1-2 2A17 17 0 0 1 3 5a2 2 0 0 1 2-2z"/></svg>
      <div>+4740012345</div>
    </div>
    <div class="footer-row">
      <svg width="12" height="10" viewBox="0 0 12 10" style="margin-top:6px" fill="none" stroke="#2a1512"><rect x=".5" y=".5" width="11" height="9"/><path d="M.5.5 6 5.5 11.5.5"/></svg>
      <div>post@lunaform-example.no</div>
    </div>
  </div>

  <h4 class="abs footer-head" style="left:887px">FOLLOW US</h4>
  <ul class="abs social" style="left:884px;top:118px">
    <li><i></i>Chatterloop</li>
    <li><i></i>Chirpwave</li>
    <li><i></i>Linkwell</li>
    <li><i></i>Pixelane</li>
  </ul>

  <div class="abs footer-rule"></div>
  <p class="abs copyright">Copyright © 2020 Lunaform Farge &amp; interiordesign. All Rights Reserved</p>
</footer>

</body>
</html>
```